Hi everyone,
Clear Path Homes is a business that renovates older houses into modern homes. I'm looking for a design that is clean and simple. It needs to show the client that renovating is a simple process. No more than 3 colours to be used thanks.

What I need:
1. Logo
2. Business card (one side)
3. Letter head (A4)

Looking forward to the designs!

Industry/Entity Type

Construction

Logo Text

Clear Path Homes

Font styles to use
Sans Serif

Requirements
Must have
• Trading name: Clear Path Homes
• Contact name: Daniel Whitcombe
• Email: danielwhitcombe@clearpathhomes.com.au
• Tel: 0412 758 204
• Clean and simple
Nice to have
• If design might include a few tools. eg Hammer, paint roller etc.
Should not have
• Complicated design

```html
<!DOCTYPE html>
<html lang="en">
<head>
<meta charset="utf-8">
<title>Clear Path Homes — Business Card</title>
<link rel="stylesheet" href="https://fonts.googleapis.com/css2?family=Arimo&family=Questrial&display=swap">
<style>
  :root {
    --card-bg: #e6e6e6;
    --band-grey: #646464;
    --ink: #444444;
    --ink-soft: #a9a9a9;
    --accent: #f9b03c;
  }
  html, body {
    margin: 0;
    padding: 0;
    width: 1200px;
    height: 700px;
    overflow: hidden;
    background: var(--card-bg);
  }
  .business-card {
    position: relative;
    width: 1200px;
    height: 700px;
    background: var(--card-bg);
    overflow: hidden;
  }
  .side-band {
    position: absolute;
    top: 0;
    right: 0;
    width: 170px;
    height: 700px;
    background: var(--band-grey);
  }
  .brand {
    position: absolute;
    left: 84px;
    top: 254px;
    display: flex;
    align-items: flex-start;
    gap: 18px;
  }
  .brand-name {
    margin: 0;
    font-family: "Arimo", Arial, sans-serif;
    font-weight: 400;
    font-size: 66px;
    line-height: 1;
    color: var(--ink);
    letter-spacing: 0.5px;
    white-space: nowrap;
  }
  .brand-mark {
    width: 48px;
    height: 48px;
    background: var(--accent);
    margin-top: 2px;
  }
  .tagline {
    position: absolute;
    left: 84px;
    top: 336px;
    margin: 0;
    font-family: "Questrial", "Century Gothic", sans-serif;
    font-size: 40px;
    line-height: 1.1;
    color: var(--ink-soft);
  }
  .contact {
    position: absolute;
    left: 84px;
    top: 482px;
    font-family: "Questrial", "Century Gothic", sans-serif;
    color: var(--ink);
  }
  .contact-name {
    margin: 0 0 14px;
    font-weight: 400;
    font-size: 54px;
    line-height: 1.1;
  }
  .contact-line {
    margin: 0 0 11px 6px;
    font-size: 20px;
    line-height: 1.1;
  }
</style>
</head>
<body>
  <main class="business-card">
    <div class="side-band" role="img" aria-label="Grey decorative band along the right edge"></div>

    <div class="brand">
      <h1 class="brand-name">CLEAR PATH HOMES</h1>
      <span class="brand-mark"></span>
    </div>
    <p class="tagline">Clean and Simple</p>

    <section class="contact">
      <h2 class="contact-name">Daniel Whitcombe</h2>
      <p class="contact-line">0412 758 204</p>
      <p class="contact-line">danielwhitcombe@clearpathhomes.com.au</p>
    </section>
  </main>
</body>
</html>
```